Web Design needed for business consultancy

Need a new webpage for a business consultancy that targets small to medium sized businesses. For "feel" please look at https://www.vrelto-example.com/index_e.htm. Key ideas we are trying to get across are our global expertise, and professionalism. Font and Logo as per the attached proofsheet. Need the ability to edit and add content, and to link to ventorra and plumbox is critical

Project Deadline Extended Reason: Just launched this part of the rebranding project. If futher extensions are required, I will look into this. Added Monday, March 9, 2015

Reason: Time to finalise designs with current submitting designer, and to consider any alternatives

Target Market(s)

Small to Medium Sized Business

Industry/Entity Type

Business

Number of Pages Required

5+ page

Requirements
Must have
• Logos, colours and fonts as per the logo work
• Ability to edit and add content and link to plumbox and ventorra
• Clicking on my email leads to a new email using my address
Nice to have
• Some appropriate photo artwork
• Clocks on the front page (or all pages?) that show the correct time in 6 cities
Should not have
• Nothing too folksy

```html
<!DOCTYPE html>
<html lang="en">
<head>
<meta charset="utf-8">
<title>Norvane Partners — About Us</title>
<link href="https://fonts.googleapis.com/css2?family=Dosis:wght@400;500;600;700&family=Source+Sans+3:wght@300;400&display=swap" rel="stylesheet">
<style>
  :root {
    --navy: #0b3663;
    --navy-deep: #063160;
    --sky: #5aaee0;
    --icon-blue: #4aa3dc;
    --ink: #1d1d1d;
    --body-text: #4a4f55;
    --tagline: #5a6a7c;
    --rule: #e6e9ee;
    --white: #ffffff;
  }
  * { margin: 0; padding: 0; box-sizing: border-box; }
  html, body { width: 1200px; height: 815px; overflow: hidden; background: var(--white); }
  .page { position: relative; width: 1200px; height: 815px; overflow: hidden; font-family: "Source Sans 3", sans-serif; }

  .top-line { position: absolute; top: 0; left: 0; width: 100%; height: 2px; background: var(--sky); }

  .site-header {
    position: absolute; top: 2px; left: 0; width: 100%; height: 123px;
    background: linear-gradient(90deg, #f3f5f8 0%, #fafbfc 40%, #f1f4f7 100%);
  }
  .brand { position: absolute; left: 100px; top: 44px; display: flex; flex-direction: column; }
  .brand-name {
    font-family: "Dosis", sans-serif; font-weight: 700; font-size: 30px;
    letter-spacing: 2.5px; color: var(--navy); line-height: 1;
  }
  .brand-tagline {
    font-family: "Dosis", sans-serif; font-weight: 600; font-size: 10px;
    letter-spacing: 1px; color: var(--tagline); margin-top: 5px;
  }

  .main-nav { position: absolute; top: 46px; right: 100px; display: flex; align-items: center; }
  .main-nav a {
    font-family: "Dosis", sans-serif; font-weight: 500; font-size: 14px;
    color: var(--ink); text-decoration: none; letter-spacing: 0.3px;
    padding: 0 30px; line-height: 36px; border-left: 1px solid var(--rule);
  }
  .main-nav a:first-child, .main-nav a:nth-child(2) { border-left: none; }
  .main-nav a.is-active { background: var(--navy); color: var(--white); border-radius: 3px; padding: 0 21px; margin-right: 0; }
  .main-nav a:last-child { padding-right: 0; }

  .hero-band {
    position: absolute; top: 125px; left: 0; width: 100%; height: 160px;
    background: linear-gradient(180deg, #50698a 0%, #3c5b82 55%, #2f4e78 100%);
  }

  .content-card {
    position: absolute; top: 215px; left: 99px; width: 1002px; height: 500px;
    background: var(--white); border-radius: 4px 4px 0 0;
  }
  .section-title {
    position: absolute; top: 30px; left: 0; width: 100%; text-align: center;
    font-family: "Dosis", sans-serif; font-weight: 600; font-size: 30px;
    letter-spacing: -1px; color: var(--navy);
  }

  .features { position: absolute; top: 303px; left: 125px; display: flex; gap: 23px; }
  .feature { width: 220px; text-align: center; }
  .feature-photo { width: 220px; height: 162px; }
  .photo-globe { background: linear-gradient(160deg, #c9a66b 0%, #8c7d72 45%, #3b3a3d 100%); }
  .photo-screen { background: linear-gradient(150deg, #3a9ee0 0%, #7cc6ef 55%, #cfe9f8 100%); }
  .photo-meeting { background: linear-gradient(140deg, #dfe6ee 0%, #6d86a6 50%, #1d3150 100%); }
  .photo-chart { background: linear-gradient(150deg, #eef1f3 0%, #d5dde4 55%, #b9c5cf 100%); }
  .feature-icon { display: block; margin: 24px auto 0; width: 44px; height: 44px; }
  .feature-text {
    margin-top: 16px; font-weight: 300; font-size: 14.5px; line-height: 22px; color: var(--body-text);
  }

  .site-footer { position: absolute; top: 707px; left: 0; width: 100%; height: 108px; background: var(--navy-deep); }
  .footer-links { position: absolute; top: 25px; left: 99px; font-size: 14.5px; color: var(--white); }
  .footer-links a { color: var(--white); text-decoration: none; }
  .footer-links span { margin: 0 6px; }
  .copyright { position: absolute; top: 60px; left: 99px; font-size: 12.5px; color: var(--white); }
  .social { position: absolute; top: 43px; left: 964px; display: flex; gap: 5px; }
  .social a { width: 24px; height: 24px; border: 1.5px solid rgba(255,255,255,0.85); border-radius: 50%; display: block; }
</style>
</head>
<body>
<div class="page">
  <div class="top-line"></div>

  <header class="site-header">
    <div class="brand">
      <span class="brand-name">NORVANE PARTNERS</span>
      <span class="brand-tagline">WORLDWIDE INSIGHT | REGIONAL ADVICE</span>
    </div>
    <nav class="main-nav">
      <a href="#" class="is-active">HOME</a>
      <a href="#">ABOUT</a>
      <a href="#">SERVICES</a>
      <a href="#">TESTIMONIALS</a>
      <a href="#">COMMENTARY</a>
      <a href="#">CONTACT</a>
    </nav>
  </header>

  <div class="hero-band" role="img" aria-label="City skyline with clock tower under a blue-tinted sky"></div>

  <section class="content-card">
    <h1 class="section-title">About Us : Norvane Partners</h1>
  </section>

  <div class="features">
    <article class="feature">
      <div class="feature-photo photo-globe" role="img" aria-label="Businesswoman holding a globe above the clouds"></div>
      <svg class="feature-icon" viewBox="0 0 44 44" aria-hidden="true">
        <circle cx="22" cy="22" r="20" fill="var(--icon-blue)"/>
        <path d="M10 14 q6 -4 10 0 q2 5 -2 8 q-4 1 -3 6 q-4 -2 -5 -7z M26 20 q5 -2 8 2 q1 6 -3 10 q-3 -1 -3 -5 q-3 -3 -2 -7z" fill="var(--white)"/>
      </svg>
      <p class="feature-text">We provide access our Global Experience and local contacts</p>
    </article>
    <article class="feature">
      <div class="feature-photo photo-screen" role="img" aria-label="Woman touching a digital world map interface"></div>
      <svg class="feature-icon" viewBox="0 0 60 44" aria-hidden="true" style="width:60px">
        <path d="M2 2 V41 H58" fill="none" stroke="var(--icon-blue)" stroke-width="3"/>
        <path d="M7 39 V25 L15 18 L24 27 L34 13 L48 31 L54 39z" fill="var(--icon-blue)"/>
      </svg>
      <p class="feature-text">Our global reach gives us unique access to capital and opportunities to help you grow</p>
    </article>
    <article class="feature">
      <div class="feature-photo photo-meeting" role="img" aria-label="Two businessmen reviewing a tablet at a desk"></div>
      <svg class="feature-icon" viewBox="0 0 44 44" aria-hidden="true">
        <g fill="var(--icon-blue)">
          <circle cx="22" cy="22" r="14"/>
          <rect x="18" y="1" width="8" height="10" rx="1"/>
          <rect x="18" y="33" width="8" height="10" rx="1"/>
          <rect x="1" y="18" width="10" height="8" rx="1"/>
          <rect x="33" y="18" width="10" height="8" rx="1"/>
          <rect x="18" y="1" width="8" height="10" rx="1" transform="rotate(45 22 22)"/>
          <rect x="18" y="33" width="8" height="10" rx="1" transform="rotate(45 22 22)"/>
          <rect x="1" y="18" width="10" height="8" rx="1" transform="rotate(45 22 22)"/>
          <rect x="33" y="18" width="10" height="8" rx="1" transform="rotate(45 22 22)"/>
        </g>
        <circle cx="22" cy="22" r="6" fill="var(--white)"/>
      </svg>
      <p class="feature-text">We provide independent advice to small and mid-sized companies, delivering service levels and solutions usually only available to larger corporates</p>
    </article>
    <article class="feature">
      <div class="feature-photo photo-chart" role="img" aria-label="Hand holding a rising blue bar chart"></div>
      <svg class="feature-icon" viewBox="0 0 52 44" aria-hidden="true" style="width:52px">
        <path d="M18 8 V4 h16 v4" fill="none" stroke="var(--icon-blue)" stroke-width="3.5"/>
        <rect x="0" y="8" width="52" height="16" rx="3" fill="var(--icon-blue)"/>
        <rect x="0" y="26" width="52" height="16" rx="3" fill="var(--icon-blue)"/>
        <rect x="22" y="21" width="8" height="7" fill="var(--white)"/>
      </svg>
      <p class="feature-text">We are completely independent of the both the investment and commercial banks, but our knowledge and experience of these institutions provides you with a strong voice at the</p>
    </article>
  </div>

  <footer class="site-footer">
    <nav class="footer-links">
      <a href="#">Home</a><span>/</span><a href="#">About Us</a><span>/</span><a href="#">Our Services</a><span>/</span><a href="#">Events</a><span>/</span><a href="#">Contact Us</a>
    </nav>
    <p class="copyright">©2014 - 2015&nbsp; Norvane , All Rights Reserved.</p>
    <div class="social">
      <a href="#" aria-label="Social link 1"></a>
      <a href="#" aria-label="Plumbox"></a>
      <a href="#" aria-label="Social link 3"></a>
      <a href="#" aria-label="Social link 4"></a>
      <a href="#" aria-label="Ventorra"></a>
    </div>
  </footer>
</div>
</body>
</html>
```